Presentation Folder

We are looking for a presentation folder design that will allow us to bring our proposals/quotes to clients and leave with them. The front cover should have our logo as well as show some of the products we sell: IT Networking equipment, WiFi, Servers/Storage.
Inside flap has an area for our business cards.

Target Market(s)

Mid Sized Businesses and Private Education. Business to Business. IT Directors. Ages 30 to 50. College Educated. Southern California

Industry/Entity Type

Business

Logo Text

Requirements
Must have
• Our Logo
Complimentary color schemes to our logo.
Should be Professional.

```html
<!DOCTYPE html>
<html lang="en">
<head>
<meta charset="utf-8">
<title>Corvanta Presentation Folder</title>
<link rel="stylesheet" href="https://fonts.googleapis.com/css2?family=Raleway:wght@300;400&family=Lato:wght@400;700&display=swap">
<style>
  :root {
    --stage: #e4e4e4;
    --cover-light: #eef6fb;
    --sky: #1ab1de;
    --sky-soft: #8fd3ec;
    --sky-pale: #c6e8f5;
    --teal-band: #1f7d97;
    --ink: #555a5f;
    --charcoal: #3c3d3f;
    --orange: #e47d26;
    --panel-white: #fbfbfb;
    --panel-grey: #dcdcdc;
    --card-black: #1e1e1e;
    --server-grey: #8d939a;
    --device-white: #ecebe6;
    --board-green: #5f7458;
  }
  * { box-sizing: border-box; margin: 0; padding: 0; }
  html, body { width: 1200px; height: 847px; overflow: hidden; }
  body { background: var(--stage); position: relative; font-family: "Lato", sans-serif; }

  .panel { position: absolute; overflow: hidden; box-shadow: 0 6px 18px rgba(0,0,0,.12); }

  .wordmark {
    font-family: "Raleway", sans-serif; font-weight: 300;
    letter-spacing: 1px; color: var(--ink); white-space: nowrap;
  }

  /* Front cover */
  .front-cover { left: 70px; top: 255px; width: 290px; height: 440px; background: var(--cover-light); }
  .corner-accent {
    position: absolute; left: 0; top: 0; width: 160px; height: 160px;
    background: radial-gradient(circle at 0 0, var(--sky) 0, var(--sky-soft) 40%, var(--sky-pale) 65%, rgba(238,246,251,0) 80%);
  }
  .front-cover .wordmark { position: absolute; top: 148px; width: 100%; text-align: center; font-size: 32px; }
  .front-cover .rule { position: absolute; height: 2px; background: var(--sky); }
  .front-cover .rule.upper { top: 232px; left: 85px; width: 120px; }
  .front-cover .rule.lower { top: 332px; left: 28px; width: 90px; }
  .product-band { position: absolute; left: 0; top: 242px; width: 100%; height: 80px; background: var(--teal-band); }
  .product-photos { position: absolute; left: 8px; top: 8px; width: 274px; height: 64px; display: flex; gap: 10px; }
  .product-photos span { flex: 1; border-radius: 4px; }
  .product-photos .servers { background: linear-gradient(180deg, #b7bcc1, var(--server-grey)); }
  .product-photos .access-point { background: linear-gradient(180deg, #fbfaf6, var(--device-white)); }
  .product-photos .circuit-board { background: linear-gradient(180deg, #7d9174, var(--board-green)); border-radius: 50%; flex: 0 0 64px; }

  /* Inside spread */
  .inside-spread { left: 380px; top: 105px; width: 440px; height: 335px; }
  .inside-left { position: absolute; left: 0; top: 0; width: 220px; height: 100%; background: var(--panel-white); }
  .inside-right { position: absolute; left: 220px; top: 0; width: 220px; height: 100%; background: var(--panel-grey); }
  .pocket { position: absolute; bottom: 0; width: 100%; height: 95px; }
  .pocket.charcoal { background: var(--charcoal); }
  .pocket.orange { background: var(--orange); }
  .pocket.charcoal .wordmark { position: absolute; left: 0; top: 30px; width: 100%; text-align: center; font-size: 27px; color: #d8d8d8; }
  .business-card {
    position: absolute; left: 50px; top: 16px; width: 112px; height: 62px;
    background: var(--card-black); border: 1px solid #000; padding: 5px 8px; color: #dcdcdc;
  }
  .business-card .wordmark { font-size: 13px; color: #e6e6e6; }
  .business-card p { font-size: 5.5px; line-height: 7px; margin-top: 2px; }

  /* Back cover */
  .back-cover { left: 870px; top: 245px; width: 280px; height: 450px; background: var(--sky); }
  .back-cover .swoosh { position: absolute; left: 0; top: 0; }
  .back-cover .footer-band { position: absolute; left: 0; bottom: 40px; width: 100%; height: 70px; background: #fff; }
  .back-cover .wordmark { position: absolute; left: 12px; top: 24px; font-size: 20px; }
  .back-cover address { position: absolute; left: 140px; top: 14px; font-style: normal; font-size: 6px; line-height: 8px; color: var(--ink); }
</style>
</head>
<body>

  <section class="panel front-cover" aria-label="Front cover">
    <div class="corner-accent" role="img" aria-label="Decorative blue corner accent"></div>
    <div class="wordmark">CORVANTA</div>
    <div class="rule upper"></div>
    <div class="product-band">
      <div class="product-photos" role="img" aria-label="Product photos: rack servers, a wireless access point and a network circuit board">
        <span class="servers"></span>
        <span class="access-point"></span>
        <span class="circuit-board"></span>
      </div>
    </div>
    <div class="rule lower"></div>
  </section>

  <section class="panel inside-spread" aria-label="Inside spread">
    <div class="inside-left">
      <div class="pocket charcoal"><div class="wordmark">CORVANTA</div></div>
    </div>
    <div class="inside-right">
      <div class="pocket orange">
        <div class="business-card">
          <div class="wordmark">CORVANTA</div>
          <p>2240 Harbor Way, Suite 310<br>Bayview, CA 90000<br>555-014-2290<br>www.corvanta.com</p>
        </div>
      </div>
    </div>
  </section>

  <section class="panel back-cover" aria-label="Back cover">
    <svg class="swoosh" width="280" height="450" viewBox="0 0 280 450">
      <path d="M170 0 Q 260 120 280 150 L280 0 Z" fill="#3cbfe4"/>
      <path d="M0 335 Q 140 290 280 300 L280 450 L0 450 Z" fill="#55c8ea"/>
    </svg>
    <div class="footer-band">
      <div class="wordmark">CORVANTA</div>
      <address>Corporate Headquarters<br>2240 Harbor Way, Suite 310<br>Bayview, CA 90000<br>555-014-2290<br>www.corvanta.com</address>
    </div>
  </section>

</body>
</html>
```